Mobile Recording Studio needs business cards

Open to seeing a creative design, but I want to emphasis my logo and minimize the name/title and company information. Possible a fully black background on card.

My company is a mobile sound recording studio. ok to include a my trailer (actual or cartoon) on the card. My initial thought is more straight forward, but a good design will win me over.

SPECS:
CMYK color mode
High (300ppi) raster effect.
cover bleed area
please deliver: Illustrator file with layers and a pdf at completion.

Name and info for the business card:

Dallin Perry
ADR Mixer

email: Dallin@MixVault.com

address:
248 - 5170 East Hollister
Vancouver, BC V5R 2J4

phone:
604.518.2093 office

website:
www.MixVault.com

FB: @MixVault

Instagram: @TheMixVault

Industry/Entity Type

Television Production

Contact Information for Business Card

Dallin Perry
ADR Mixer

email: Dallin@MixVault.com

address:
248 - 5170 East Hollister
Vancouver, BC V5R 2J4

phone:
604.518.2093 office

website:
www.MixVault.com

FB: @MixVault

Instagram: @TheMixVault

Colors

Designer to choose colors to be used in the design.

Requirements
Must have
• emphasis my logo and minimize the name/title and company information.
• SPECS:
• CMYK color mode
• High (300ppi) raster effect.
• cover bleed area
• please deliver: Illustrator file with layers and a pdf at completion.
Nice to have
• maybe include the following:
• all black background or black theme
• my work trailer (actual or cartoon) refer to Instagram: @TheMixVault

```html
<!DOCTYPE html>
<html lang="en">
<head>
<meta charset="utf-8">
<title>MixVault – Business Card</title>
<link rel="stylesheet" href="https://fonts.googleapis.com/css2?family=Cinzel:wght@500;600&family=Lato:wght@400&display=swap">
<style>
  :root {
    --page-bg: #212528;
    --card-front: #000000;
    --card-back: #0b0000;
    --ink: #f0f0f0;
    --silver: #c9cacc;
    --icon: #e6e6e6;
    --photo-sky: #1f2e52;
    --photo-top: #2a3d68;
    --photo-mid: #3b5585;
    --photo-low: #5f7598;
    --photo-ground: #8da0bb;
  }
  * { margin: 0; padding: 0; box-sizing: border-box; }
  html, body { width: 1200px; height: 1176px; overflow: hidden; }
  body { background: var(--page-bg); position: relative; font-family: "Lato", Arial, sans-serif; }

  .card {
    position: absolute;
    left: 280px;
    width: 618px;
    height: 352px;
    border-radius: 22px;
    overflow: hidden;
    box-shadow: 0 10px 22px rgba(0,0,0,0.45);
  }
  .card-front { top: 190px; background: var(--card-front); }
  .card-back { top: 590px; background: var(--card-back); }

  .brand-name {
    position: absolute;
    left: 40px;
    top: 145px;
    width: 250px;
    text-align: center;
    font-family: "Cinzel", Georgia, serif;
    font-weight: 600;
    font-size: 40px;
    letter-spacing: 1px;
    color: var(--silver);
  }

  .contact { position: absolute; left: 323px; top: 52px; color: var(--ink); }
  .person-name {
    font-family: "Cinzel", Georgia, serif;
    font-weight: 500;
    font-size: 22px;
    letter-spacing: 0.5px;
    line-height: 1;
  }
  .person-title {
    font-family: "Cinzel", Georgia, serif;
    font-weight: 500;
    font-size: 16px;
    margin-top: 11px;
    line-height: 1;
  }
  .details { list-style: none; margin-top: 24px; font-size: 15.5px; line-height: 25px; }
  .details li { display: flex; align-items: flex-start; }
  .details .icon { width: 12px; height: 12px; margin: 7px 8px 0 0; flex: none; }
  .icon-solid { fill: var(--icon); }
  .icon-line { fill: none; stroke: var(--icon); stroke-width: 1; }
  .details .gap { margin-top: 6px; }
  .socials { display: flex; gap: 16px; margin-top: 17px; font-size: 15.5px; }
  .socials span { display: flex; align-items: center; }
  .social-mark { width: 12px; height: 12px; background: var(--icon); border-radius: 2px; margin-right: 8px; }

  .trailer-photo { position: absolute; inset: 0; }
</style>
</head>
<body>

<section class="card card-front">
  <div class="brand-name">MixVault</div>

  <div class="contact">
    <div class="person-name">Dallin Perry</div>
    <div class="person-title">ADR Mixer</div>
    <ul class="details">
      <li>
        <svg class="icon icon-solid" viewBox="0 0 12 12"><path d="M6 0a4 4 0 0 0-4 4c0 3 4 8 4 8s4-5 4-8a4 4 0 0 0-4-4zm0 5.6A1.6 1.6 0 1 1 6 2.4a1.6 1.6 0 0 1 0 3.2z"/></svg>
        <span>248 - 5170 East Hollister<br>Vancouver, BC V5R 2J4</span>
      </li>
      <li class="gap">
        <svg class="icon" viewBox="0 0 12 12"><rect class="icon-line" x="0.7" y="2.5" width="10.6" height="7.5"/><path class="icon-solid" d="M0.7 2.5h10.6L6 7z"/></svg>
        <span>Dallin@MixVault.com</span>
      </li>
      <li>
        <svg class="icon icon-solid" viewBox="0 0 12 12"><path d="M3 0.5 5 3 3.8 4.5c.6 1.5 1.8 2.8 3.4 3.6L8.6 7 11.5 9 10 11.5C5 11 1 7 .5 2z"/></svg>
        <span>604.518.2093</span>
      </li>
      <li>
        <svg class="icon icon-line" viewBox="0 0 12 12"><circle cx="6" cy="6" r="5.3"/><ellipse cx="6" cy="6" rx="2.3" ry="5.3"/><path d="M0.7 6h10.6M1.5 3.3h9M1.5 8.7h9"/></svg>
        <span>www.MixVault.com</span>
      </li>
    </ul>
    <div class="socials">
      <span><i class="social-mark"></i>@MixVault</span>
      <span><i class="social-mark"></i>@TheMixVault</span>
    </div>
  </div>
</section>

<section class="card card-back">
  <svg class="trailer-photo" viewBox="0 0 618 352" width="618" height="352" role="img" aria-label="Photo of the mobile recording studio trailer, branded with the company name, parked beside a box truck outside a studio building">
    <defs>
      <linearGradient id="photoTone" x1="0" y1="0" x2="0" y2="1">
        <stop offset="0" stop-color="var(--photo-sky)"/>
        <stop offset="0.3" stop-color="var(--photo-top)"/>
        <stop offset="0.62" stop-color="var(--photo-mid)"/>
        <stop offset="0.8" stop-color="var(--photo-low)"/>
        <stop offset="1" stop-color="var(--photo-ground)"/>
      </linearGradient>
    </defs>
    <path d="M0 75 Q309 -21 618 75 L618 277 Q309 375 0 277 Z" fill="url(#photoTone)"/>
  </svg>
</section>

</body>
</html>
```